Business card design needed

It's a new business in town.Something so the name stands out.I need a logo for the B.R.W
I may all so use the design as a sign on a building

Contact Information for Business Card

B.R.W
Brindlewood Auto Detailing
42 Fenwarra Crs
Brindlewood Vic 3799
Ph:(03)59284736
Mob:0417362958

```html
<!DOCTYPE html>
<html lang="en">
<head>
<meta charset="utf-8">
<title>Brindlewood Auto Detailing – Business Card</title>
<link rel="stylesheet" href="https://fonts.googleapis.com/css2?family=Cinzel:wght@900&family=Didact+Gothic&display=swap">
<style>
  :root {
    --page: #ffffff;
    --card: #040506;
    --brand-blue: #1f7fd1;
    --contact: #8aa3b8;
    --chrome-light: #f4f6f8;
    --chrome-mid: #9aa0a6;
    --chrome-dark: #3b3f44;
  }
  html, body {
    margin: 0;
    width: 1200px;
    height: 672px;
    overflow: hidden;
    background: var(--page);
  }
  .card {
    position: absolute;
    left: 29px;
    top: 26px;
    width: 1151px;
    height: 624px;
    background: var(--card);
    font-family: "Didact Gothic", sans-serif;
  }
  .brand-mark {
    position: absolute;
    left: 0;
    right: 0;
    top: 78px;
    text-align: center;
    color: var(--brand-blue);
    font-size: 118px;
    line-height: 1;
    letter-spacing: 6px;
  }
  .business-name {
    position: absolute;
    left: 0;
    right: 0;
    top: 366px;
    margin: 0;
    text-align: center;
    font-family: "Cinzel", serif;
    font-weight: 900;
    font-size: 58px;
    line-height: 1;
    letter-spacing: 1px;
    background: linear-gradient(180deg,
      var(--chrome-light) 0%,
      var(--chrome-light) 30%,
      var(--chrome-mid) 50%,
      var(--chrome-dark) 56%,
      var(--chrome-mid) 75%,
      var(--chrome-light) 100%);
    -webkit-background-clip: text;
    background-clip: text;
    color: transparent;
  }
  .address, .phones {
    position: absolute;
    margin: 0;
    color: var(--contact);
    font-style: normal;
  }
  .address {
    left: 139px;
    top: 488px;
    font-size: 32px;
    line-height: 36px;
    letter-spacing: 1px;
  }
  .phones {
    left: 706px;
    top: 506px;
    font-size: 35px;
    line-height: 48px;
  }
  .phones p { margin: 0; }
</style>
</head>
<body>
  <main class="card">
    <div class="brand-mark">B.R.W</div>
    <h1 class="business-name">Brindlewood Auto Detailing</h1>
    <address class="address">
      42 Fenwarra Crs<br>
      Brindlewood<br>
      Vic 3799
    </address>
    <div class="phones">
      <p>Ph: (03) 5928 4736</p>
      <p>Mob: 0417 362 958</p>
    </div>
  </main>
</body>
</html>
```